" Clinica de radiologia especializada em diagnóstico para odontologia. Compromisso com a qualidade e tecnologia de seus equipamentos. Mais de 50 mil pacientes atendidos. "

```html
<!DOCTYPE html>
<html lang="pt-BR">
<head>
<meta charset="utf-8">
<title>Pasta de Documentos – Lumen Radiologia</title>
<link href="https://fonts.googleapis.com/css2?family=Open+Sans:wght@400;600;700&display=swap" rel="stylesheet">
<style>
  :root{
    --bg:#ffffff;
    --ink:#222222;
    --outline:#1a1a1a;
    --brand-grey:#6d6e71;
    --brand-green:#1f6b45;
    --green-band:#2f7a52;
  }
  *{margin:0;padding:0;box-sizing:border-box}
  html,body{width:1200px;height:1200px;overflow:hidden;background:var(--bg);font-family:"Open Sans",Arial,sans-serif}
  .canvas{position:relative;width:1200px;height:1200px}
  .sheet-label{position:absolute;left:12px;top:66px;font-size:17px;font-weight:700;color:var(--ink);letter-spacing:.5px}
  .dieline{position:absolute;left:0;top:0}
  .back-decoration{position:absolute;left:149px;top:163px;width:470px;height:420px;
    background:linear-gradient(180deg, rgba(255,255,255,.10) 0%, rgba(255,255,255,0) 100%);}
  .back-info{position:absolute;left:300px;top:612px;width:310px;color:#fff}
  .back-info .brand{display:flex;align-items:center;gap:7px;margin-left:14px;white-space:nowrap}
  .brand-dot{border-radius:50%;background:var(--brand-green);flex:none}
  .back-info .brand .brand-dot{width:12px;height:12px;background:#fff}
  .back-info .brand-name{font-size:11px;font-weight:600;letter-spacing:1.5px;color:#fff}
  .back-info .tagline{margin-top:18px;font-size:9px;font-weight:700;line-height:1.35;white-space:nowrap}
  .back-info .contact{font-size:8.5px;line-height:1.45;white-space:nowrap}
  .front-brand{position:absolute;left:680px;top:460px;width:330px;display:flex;align-items:center;gap:12px;justify-content:center;white-space:nowrap}
  .front-brand .brand-dot{width:24px;height:24px}
  .front-brand .brand-name{font-size:24px;font-weight:600;letter-spacing:2px;color:var(--brand-grey);line-height:1}
</style>
</head>
<body>
<div class="canvas">
  <div class="sheet-label">PASTA DE DOCUMENTOS</div>

  <svg class="dieline" width="1200" height="1200" viewBox="0 0 1200 1200">
    <defs>
      <linearGradient id="backPanel" x1="0" y1="0" x2="0" y2="1">
        <stop offset="0" stop-color="#b2b3b5"/>
        <stop offset="1" stop-color="#a3a4a6"/>
      </linearGradient>
      <linearGradient id="frontPanel" x1="0" y1="0" x2="1" y2="0">
        <stop offset="0" stop-color="#e4e4e5"/>
        <stop offset=".35" stop-color="#fbfbfb"/>
        <stop offset="1" stop-color="#ececed"/>
      </linearGradient>
      <linearGradient id="pocket" x1="0" y1="0" x2="1" y2="1">
        <stop offset="0" stop-color="#a9aaac"/>
        <stop offset="1" stop-color="#939496"/>
      </linearGradient>
    </defs>

    <path d="M1056 163 L1066 163 L1076 178 L1076 763 L1056 775" fill="none" stroke="var(--outline)" stroke-width="2"/>

    <rect x="149" y="163" width="470" height="600" fill="url(#backPanel)"/>
    <rect x="619" y="163" width="437" height="600" fill="url(#frontPanel)"/>

    <rect x="149" y="748" width="907" height="10" fill="var(--green-band)"/>
    <rect x="149" y="758" width="907" height="5" fill="#cfd3d0"/>

    <path d="M149 790 L80 810 L80 1118 L149 1135 Z" fill="#ffffff" stroke="var(--outline)" stroke-width="2"/>

    <path d="M149 763 L619 763 L619 955 C540 975 430 990 370 1040 C320 1085 300 1130 290 1150 L149 1150 Z"
          fill="url(#pocket)" stroke="var(--outline)" stroke-width="2"/>
    <line x1="175" y1="1012" x2="196" y2="1044" stroke="#ffffff" stroke-width="2.5"/>
    <line x1="350" y1="812" x2="371" y2="845" stroke="#ffffff" stroke-width="2.5"/>
  </svg>

  <div class="back-decoration" role="img" aria-label="Área decorativa em tons de cinza claro"></div>

  <div class="back-info">
    <div class="brand">
      <span class="brand-dot"></span>
      <span class="brand-name">LUMEN RADIOLOGIA</span>
    </div>
    <p class="tagline">Clínica de Radiologia e Documentação Odontológica</p>
    <p class="contact">R. das Acácias, 210 - Centro - Vale Azul - SC</p>
    <p class="contact">(47) 3000-0000 | contato@lumenradiologia.com.br</p>
  </div>

  <div class="front-brand">
    <span class="brand-dot"></span>
    <span class="brand-name">LUMEN RADIOLOGIA</span>
  </div>
</div>
</body>
</html>
```